TBrandow executive consulting

We need a basic clean website for executive consulting. Rosalind is the previos CIO for bluecrest skyways and currently supports several technology companies with innovation and transformation.

Target Market(s)

C level technology and CIO training

Industry/Entity Type

Technology and travel industry

Coding

Coded - Design and coding required

Number of Pages Required

3 page

Font styles to use
Sans Serif

Colors
0054AA
0677BA
7BADD7
CADEEF
E8F1F8
0094D4
00A9DD
6FCCEA
C7EBF8
E9F6FB

Requirements
Must have
• Home page, about us, services social media links

```html
<!DOCTYPE html>
<html lang="en">
<head>
<meta charset="utf-8">
<title>TBrandow Executive Consulting</title>
<link href="https://fonts.googleapis.com/css2?family=Poppins:wght@400;500;600;700&family=Marcellus&display=swap" rel="stylesheet">
<style>
:root{
  --navy:#0054AA;
  --ocean:#0677BA;
  --sky:#00A9DD;
  --azure:#0094D4;
  --aqua:#6FCCEA;
  --mist:#C7EBF8;
  --ice:#E9F6FB;
  --pale:#E8F1F8;
  --ink:#1d1d1f;
  --text:#333;
  --white:#fff;
  --black:#000;
}
*{box-sizing:border-box;margin:0;padding:0}
html,body{width:1200px;height:3559px;overflow:hidden;background:var(--white)}
body{font-family:"Poppins",sans-serif;color:var(--text)}
.page{position:relative;width:1200px;height:3559px;overflow:hidden}
.abs{position:absolute}
.btn{position:absolute;display:flex;align-items:center;justify-content:center;gap:8px;border-radius:30px;background:var(--sky);color:var(--white);font-size:14px;letter-spacing:.5px;text-decoration:none}

/* header */
.site-header{position:absolute;left:0;top:0;width:1200px;height:84px;background:var(--white);z-index:3}
.brand{position:absolute;left:142px;top:22px;display:flex;align-items:center;gap:8px;color:var(--ocean);font-weight:600;font-size:24px}
.brand-dot{width:14px;height:14px;border-radius:50%;background:var(--sky)}
.nav{position:absolute;top:34px;display:flex;gap:0;font-size:12.5px;font-weight:500;color:var(--ink)}
.nav a{position:absolute;color:var(--ink);text-decoration:none;white-space:nowrap}
.social-dot{position:absolute;top:24px;width:36px;height:36px;border:1.5px solid var(--ocean);border-radius:50%;color:var(--ocean);font-size:11px;font-weight:600;display:flex;align-items:center;justify-content:center}
.call{position:absolute;left:810px;top:18px}
.call-icon{position:absolute;left:0;top:2px;width:44px;height:44px;border:2px solid var(--ocean);border-radius:50%}
.call-label{position:absolute;left:59px;top:0;color:var(--azure);font-size:15px;font-weight:500;white-space:nowrap}
.call-number{position:absolute;left:59px;top:19px;color:var(--ink);font-size:23px;font-weight:600;letter-spacing:1.5px;white-space:nowrap}

/* hero */
.hero-photo{position:absolute;left:0;top:84px;width:1200px;height:620px;background:linear-gradient(90deg,#2c3644 0%,#4a5563 40%,#5d6570 60%,#7a3a3e 80%,#5b6370 100%)}
.hero-kicker{position:absolute;left:142px;top:218px;color:var(--white);font-size:25px;font-weight:500;letter-spacing:.5px}
.hero-title{position:absolute;left:142px;top:258px;color:var(--white);font-family:"Marcellus",serif;font-size:58px;line-height:66px;font-weight:400}
.hero-btn{left:141px;top:425px;width:153px;height:45px;font-size:13px;font-weight:500;letter-spacing:1.5px}
.hero-wave{position:absolute;left:0;top:520px;z-index:1}

/* about */
.about-photo{position:absolute;left:155px;top:777px;width:374px;height:411px;border-radius:0 40px 0 0;background:linear-gradient(160deg,#d9d2c6,#8c7a6c 55%,#2b2f3a)}
.about-frame-v{position:absolute;left:141px;top:905px;width:4px;height:296px;background:var(--sky)}
.about-frame-h{position:absolute;left:141px;top:1197px;width:232px;height:4px;background:var(--sky)}
.about-label{position:absolute;left:595px;top:764px;color:var(--azure);font-size:23px;font-weight:500}
.about-name{position:absolute;left:672px;top:752px;color:var(--ink);font-size:35px;font-weight:600;white-space:nowrap}
.about-role{position:absolute;left:595px;top:802px;color:var(--ink);font-size:15.5px;font-weight:500;line-height:23px}
.about-copy{position:absolute;left:595px;top:856px;width:465px;font-size:14.3px;line-height:21.2px;color:var(--text)}
.about-copy p+p{margin-top:10px}
.about-btn{left:595px;top:1161px;width:141px;height:42px}

/* services */
.services{position:absolute;left:0;top:1290px;width:1200px;height:623px;background:linear-gradient(180deg,#13b2e2,#0aa8dc 60%,#1bb3e0)}
.section-title{position:absolute;left:0;width:1200px;text-align:center;font-weight:600}
.services .section-title{top:80px;color:var(--white);font-size:35px}
.service-card{position:absolute;top:159px;width:282px;height:298px;background:var(--white);border-radius:8px}
.service-icon{position:absolute;left:14px;top:16px;width:70px;height:70px;border-radius:50%;background:var(--azure)}
.service-icon svg{position:absolute;left:19px;top:19px}
.service-name{position:absolute;left:98px;top:40px;width:175px;color:var(--ink);font-size:14.5px;font-weight:500;line-height:19px}
.service-name.one{top:40px}
.service-points{position:absolute;left:0;top:113px;width:270px;list-style:none;font-size:12.6px;line-height:19px;color:var(--text)}
.service-points li{position:relative;padding-left:19px;margin-bottom:5px}
.service-points li::before{content:"";position:absolute;left:0;top:4px;border-left:7px solid var(--ocean);border-top:6px solid transparent;border-bottom:6px solid transparent}
.service-more{position:absolute;left:19px;top:260px;font-size:12.5px;color:var(--ink);font-weight:500;display:flex;align-items:center;gap:10px}
.view-all{position:absolute;left:507px;top:496px;width:185px;height:40px;border-radius:20px;background:var(--white);color:var(--ink);font-size:15px;display:flex;align-items:center;justify-content:center;gap:8px}

/* testimonials */
.testimonials-title{top:1985px;color:var(--ink);font-size:36px}
.quote-card{position:absolute;top:2063px;width:283px;height:275px;background:var(--white);border-radius:4px;box-shadow:0 4px 16px rgba(0,0,0,.09)}
.quote-card.featured{background:var(--sky);border-bottom:6px solid var(--navy);color:var(--white)}
.quote-text{position:absolute;left:26px;top:24px;width:240px;font-size:13px;line-height:23px;color:var(--ink)}
.quote-name{position:absolute;left:26px;top:152px;font-size:14.5px;font-weight:500;color:var(--ink)}
.quote-role{position:absolute;left:26px;top:175px;font-size:12.5px;color:var(--text)}
.featured .quote-text,.featured .quote-name,.featured .quote-role{color:var(--white)}
.quote-mark{position:absolute;right:38px;top:140px;font-family:"Marcellus",serif;font-size:70px;line-height:70px;color:#c9cdd6}
.featured .quote-mark{color:var(--white)}
.avatar{position:absolute;left:28px;top:210px;width:50px;height:50px;border-radius:50%;background:linear-gradient(135deg,#e0b9a0,#8a6650);border:2px solid #ddd}
.stars{position:absolute;right:26px;top:233px;color:#f49b1a;font-size:12px;letter-spacing:1px}
.featured .stars{color:var(--white)}
.arrow-btn{position:absolute;top:2175px;width:42px;height:42px;border-radius:50%;display:flex;align-items:center;justify-content:center}
.arrow-btn.prev{left:66px;background:var(--white);box-shadow:0 2px 10px rgba(0,0,0,.12)}
.arrow-btn.next{left:1089px;background:var(--sky)}
.dot{position:absolute;top:2379px;width:14px;height:14px;border-radius:50%;border:1.5px solid var(--aqua)}
.dot.active::after{content:"";position:absolute;left:2.5px;top:2.5px;width:6px;height:6px;border-radius:50%;background:var(--ocean)}

/* cta + contact */
.cta-band{position:absolute;left:0;top:2420px;width:1200px;height:740px;background:linear-gradient(180deg,var(--white) 0%,var(--white) 30%,var(--pale) 100%)}
.cta-title{top:2476px;color:var(--ink);font-size:32px;font-weight:500;line-height:48px}
.cta-btn{left:522px;top:2600px;width:158px;height:42px}
.contact-wave{position:absolute;left:0;top:2900px;z-index:1}
.contact-card{position:absolute;left:141px;top:2716px;width:917px;height:423px;background:var(--white);border:1.5px solid var(--aqua);border-bottom:none;border-radius:34px 34px 0 0;z-index:2}
.field{position:absolute;height:42px;border:1.5px solid #cfd6de;border-radius:21px;font-size:12.5px;color:#555;padding:13px 19px;background:var(--white)}
.field.area{height:85px;border-radius:18px}
.submit{left:287px;top:304px;width:337px;height:42px;font-size:14px}

/* footer */
.site-footer{position:absolute;left:0;top:3139px;width:1200px;height:420px;background:var(--black);color:var(--white)}
.footer-brand{position:absolute;left:142px;top:96px;display:flex;align-items:center;gap:8px;font-size:24px;font-weight:600}
.footer-about{position:absolute;left:142px;top:162px;width:250px;font-size:14.5px;line-height:24px}
.footer-head{position:absolute;top:88px;font-size:15.5px;font-weight:500;letter-spacing:.3px}
.footer-link{position:absolute;font-size:12.5px;left:447px}
.follow-item{position:absolute;left:609px;display:flex;align-items:center;gap:8px;font-size:14.5px}
.follow-dot{width:28px;height:28px;border:1.5px solid var(--white);border-radius:50%}
.contact-item{position:absolute;left:765px;font-size:14.5px;line-height:21px}
.contact-item b{font-weight:500}
.contact-item svg{position:absolute;left:-2px;top:4px}
.contact-item .txt{margin-left:29px}
.copyright{position:absolute;left:0;top:383px;width:1200px;text-align:center;font-size:13px}
</style>
</head>
<body>
<div class="page">

  <header class="site-header">
    <div class="brand"><span class="brand-dot"></span>TBrandow</div>
    <nav class="nav">
      <a href="#" style="left:371px">HOME</a>
      <a href="#" style="left:446px">ABOUT ME</a>
      <a href="#" style="left:551px">SERVICES</a>
    </nav>
    <span class="social-dot" style="left:649px">Lf</span>
    <span class="social-dot" style="left:695px">Wn</span>
    <span class="social-dot" style="left:742px">Sg</span>
    <div class="call">
      <span class="call-icon">
        <svg width="40" height="40" viewBox="0 0 40 40"><path d="M14 11c1-1 2-1 3 0l2 3c.6 1 .4 2-.4 2.6l-1.4 1c1 2.4 3 4.4 5.4 5.4l1-1.4c.6-.8 1.6-1 2.6-.4l3 2c1 1 1 2 0 3l-1.4 1.4c-1.2 1.2-3 1.4-4.6.6-4.6-2.2-8.2-5.8-10.4-10.4-.8-1.6-.6-3.4.6-4.6z" fill="none" stroke="#0677BA" stroke-width="1.8"/></svg>
      </span>
      <span class="call-label">CALL ME TODAY</span>
      <span class="call-number">(123) 456-7890</span>
    </div>
  </header>

  <section class="hero">
    <div class="hero-photo" role="img" aria-label="Photo of Rosalind Brandow smiling in a red blazer in front of a Bluecrest Skyways jet on a runway"></div>
    <p class="hero-kicker">CONSULTING FOR A</p>
    <h1 class="hero-title">Tech-Forward<br>Travel Experience</h1>
    <a class="btn hero-btn" href="#">CONTACT ME</a>
    <svg class="hero-wave" width="1200" height="200" viewBox="0 0 1200 200">
      <path d="M0 19 C90 100 240 140 430 130 C620 118 800 60 1010 42 C1100 36 1160 45 1200 54 L1200 200 L0 200 Z" fill="#fff"/>
      <path d="M189 140 C300 190 470 190 640 150 C790 110 900 50 1015 52 C900 60 800 120 640 165 C470 205 300 195 189 140 Z" fill="#0094D4"/>
    </svg>
  </section>

  <section class="about">
    <div class="about-frame-v"></div>
    <div class="about-frame-h"></div>
    <div class="about-photo" role="img" aria-label="Portrait of Rosalind Brandow in a dark blazer in a bright office"></div>
    <span class="about-label">About</span>
    <h2 class="about-name">ROSALIND BRANDOW</h2>
    <p class="about-role">Former Chief Information Officer, Bluecrest Skyways<br>Harbor Point, FL</p>
    <div class="about-copy">
      <p>Rosalind Brandow is a seasoned leader with a remarkable 40-year career in the travel industry, including 20 transformative years at Bluecrest Skyways. As the Senior Vice President of Technology (CIO), Rosalind spearheaded some of the company's most significant technological and strategic transformations, helping Bluecrest Skyways stay at the forefront of innovation in the competitive travel market. Her work bridged the gap between business strategy and technology, driving measurable success and resilience.</p>
      <p>With expertise in Leadership, Mentorship, Technology Strategy, and Digital Transformation, Rosalind is passionate about empowering IT leaders to forge stronger connections between their technology teams and business goals.</p>
    </div>
    <a class="btn about-btn" href="#">Read More
      <svg width="10" height="10" viewBox="0 0 10 10"><path d="M2 8 8 2M3 2h5v5" stroke="#fff" fill="none" stroke-width="1.2"/></svg></a>
  </section>

  <section class="services">
    <h2 class="section-title">OUR SERVICES</h2>

    <article class="service-card" style="left:141px">
      <span class="service-icon"><svg width="32" height="32" viewBox="0 0 32 32"><rect x="8" y="3" width="20" height="13" fill="none" stroke="#fff" stroke-width="1.8"/><circle cx="6" cy="14" r="3" fill="#fff"/><path d="M2 30v-8h8v8M14 30v-5h5v5M22 30v-5h5v5" fill="none" stroke="#fff" stroke-width="1.8"/></svg></span>
      <h3 class="service-name" style="top:40px">Leadership Mentorship</h3>
      <ul class="service-points">
        <li>Personalized coaching for IT leaders to develop strategic decision-making, emotional intelligence, and resilience.</li>
        <li>Mentorship programs for aspiring technology leaders to...</li>
      </ul>
      <span class="service-more">READ MORE <svg width="6" height="9" viewBox="0 0 6 9"><path d="M1 1l3.5 3.5L1 8" stroke="#0677BA" fill="none" stroke-width="1.6"/></svg></span>
    </article>

    <article class="service-card" style="left:458px">
      <span class="service-icon"><svg width="32" height="32" viewBox="0 0 32 32"><circle cx="16" cy="12" r="8" fill="none" stroke="#fff" stroke-width="1.8"/><path d="M10 30l2-8h8l2 8M16 8v8M12 12h8" fill="none" stroke="#fff" stroke-width="1.8"/></svg></span>
      <h3 class="service-name" style="top:31px">Technology Strategy Development</h3>
      <ul class="service-points">
        <li>Creating IT strategies aligned with overall business goals.</li>
        <li>Advising on IT infrastructure modernization and innovation.</li>
      </ul>
      <span class="service-more">READ MORE <svg width="6" height="9" viewBox="0 0 6 9"><path d="M1 1l3.5 3.5L1 8" stroke="#0677BA" fill="none" stroke-width="1.6"/></svg></span>
    </article>

    <article class="service-card" style="left:776px">
      <span class="service-icon"><svg width="32" height="32" viewBox="0 0 32 32"><circle cx="13" cy="16" r="9" fill="none" stroke="#fff" stroke-width="1.8"/><circle cx="13" cy="16" r="3" fill="#fff"/><path d="M22 8h6M22 16h8M22 24h6" stroke="#fff" stroke-width="1.8"/></svg></span>
      <h3 class="service-name" style="top:31px">Digital Transformation Consulting</h3>
      <ul class="service-points">
        <li>Assessing current digital maturity and identifying opportunities for improvement.</li>
        <li>Designing and implementing digital...</li>
      </ul>
      <span class="service-more">READ MORE <svg width="6" height="9" viewBox="0 0 6 9"><path d="M1 1l3.5 3.5L1 8" stroke="#0677BA" fill="none" stroke-width="1.6"/></svg></span>
    </article>

    <a class="view-all" href="#">View All Services
      <svg width="10" height="10" viewBox="0 0 10 10"><path d="M2 8 8 2M3 2h5v5" stroke="#00A9DD" fill="none" stroke-width="1.2"/></svg></a>
  </section>

  <section class="testimonials">
    <h2 class="section-title testimonials-title">TESTIMONIALS</h2>

    <span class="arrow-btn prev"><svg width="12" height="10" viewBox="0 0 12 10"><path d="M11 5H2M5 1 1 5l4 4" stroke="#1d1d1f" fill="none" stroke-width="1.6"/></svg></span>
    <span class="arrow-btn next"><svg width="12" height="10" viewBox="0 0 12 10"><path d="M1 5h9M7 1l4 4-4 4" stroke="#fff" fill="none" stroke-width="1.6"/></svg></span>

    <article class="quote-card" style="left:141px">
      <p class="quote-text">Lorem ipsum dolor sitted ametted, conse tetuer adipiscing elitteding is, seddin diam nonu mmying nibhers euismod tincidunt laoreet dolore.</p>
      <p class="quote-name">Brooklyn M.</p>
      <p class="quote-role">Lorem ipsum</p>
      <span class="quote-mark">&rdquo;</span>
      <span class="avatar" role="img" aria-label="Client portrait"></span>
      <span class="stars">★★★★★</span>
    </article>

    <article class="quote-card featured" style="left:458px">
      <p class="quote-text">Rosalind is a decisive and fair leader who exemplifies strength, wisdom, and empathy. She always possesses a clear vision for the...</p>
      <p class="quote-name">Daniel Hewitt</p>
      <p class="quote-role">CEO Northvane</p>
      <span class="quote-mark">&rdquo;</span>
      <span class="avatar" role="img" aria-label="Client portrait"></span>
      <span class="stars">★★★★★</span>
    </article>

    <article class="quote-card" style="left:776px">
      <p class="quote-text">Lorem ipsum dolor sitted ametted, conse tetuer adipiscing elitteding is, seddin diam nonu mmying nibhers euismod tincidunt laoreet dolore.</p>
      <p class="quote-name">Maria Rodri</p>
      <p class="quote-role">Lorem ipsum</p>
      <span class="quote-mark">&rdquo;</span>
      <span class="avatar" role="img" aria-label="Client portrait"></span>
      <span class="stars">★★★★★</span>
    </article>

    <span class="dot" style="left:563px"></span>
    <span class="dot active" style="left:593px"></span>
    <span class="dot" style="left:623px"></span>
  </section>

  <section class="contact">
    <div class="cta-band"></div>
    <h2 class="section-title cta-title">TAILORED SOLUTIONS FOR<br>THE FUTURE OF TRAVEL</h2>
    <a class="btn cta-btn" href="#">Get In Touch
      <svg width="10" height="10" viewBox="0 0 10 10"><path d="M2 8 8 2M3 2h5v5" stroke="#fff" fill="none" stroke-width="1.2"/></svg></a>

    <svg class="contact-wave" width="1200" height="240" viewBox="0 0 1200 240">
      <path d="M1200 50 C1120 90 1060 110 1000 130 L1000 160 C1080 140 1140 110 1200 75 Z" fill="#0094D4"/>
      <path d="M1200 75 C1130 115 1060 140 990 160 L990 240 L1200 240 Z" fill="#000"/>
      <path d="M0 180 C60 200 110 210 160 212 L160 240 L0 240 Z" fill="#000"/>
    </svg>

    <form class="contact-card">
      <div class="field" style="left:104px;top:77px;width:338px">First Name*</div>
      <div class="field" style="left:474px;top:77px;width:338px">Last Name*</div>
      <div class="field" style="left:104px;top:138px;width:338px">Your Phone*</div>
      <div class="field" style="left:474px;top:138px;width:338px">Your Email*</div>
      <div class="field area" style="left:104px;top:198px;width:708px">Your Message</div>
      <span class="btn submit">Submit Now</span>
    </form>
  </section>

  <footer class="site-footer">
    <div class="footer-brand"><span class="brand-dot"></span>TBrandow</div>
    <p class="footer-about">Lorem ipsum dolor sit amet, consectetuer adipiscing elit, seed diam nonummy nibh euismod tincidunt utted.</p>

    <h4 class="footer-head" style="left:443px">QUICK LINKS</h4>
    <span class="footer-link" style="top:128px">• Home</span>
    <span class="footer-link" style="top:166px">• About Us</span>
    <span class="footer-link" style="top:204px">• Services</span>

    <h4 class="footer-head" style="left:602px">FOLLOW US</h4>
    <span class="follow-item" style="top:130px"><span class="follow-dot"></span>Linkfeed</span>
    <span class="follow-item" style="top:170px"><span class="follow-dot"></span>Clipstream</span>
    <span class="follow-item" style="top:210px"><span class="follow-dot"></span>Snapgrid</span>
    <span class="follow-item" style="top:250px"><span class="follow-dot"></span>Chirper</span>

    <h4 class="footer-head" style="left:765px">CONTACT DETAILS</h4>
    <div class="contact-item" style="top:125px">
      <svg width="14" height="16" viewBox="0 0 14 16"><path d="M7 1a5 5 0 0 1 5 5c0 4-5 9-5 9S2 10 2 6a5 5 0 0 1 5-5z" fill="#fff"/><circle cx="7" cy="6" r="2" fill="#000"/></svg>
      <div class="txt"><b>Address</b><br>123, Building Name, Street City,<br>State XY 123456</div>
    </div>
    <div class="contact-item" style="top:194px">
      <svg width="14" height="14" viewBox="0 0 14 14"><path d="M3 1l2 3-1.4 1.4c.8 1.8 2.2 3.2 4 4L9 8l3 2-1.5 2.5C5.5 12 2 8.5 1 3.5z" fill="#fff"/></svg>
      <div class="txt"><b>Phone</b><br>(123) 456-7890</div>
    </div>
    <div class="contact-item" style="top:243px">
      <svg width="15" height="12" viewBox="0 0 15 12"><rect x="1" y="1" width="13" height="10" fill="#fff"/><path d="M1 1l6.5 5L14 1" stroke="#000" fill="none" stroke-width="1.2"/></svg>
      <div class="txt"><b>Email</b><br>info@tbrandowconsulting.com</div>
    </div>

    <p class="copyright">Copyright © 2025 Rosalind Brandow Consulting. All Rights Reserved.</p>
  </footer>

</div>
</body>
</html>
```